Harbor Sushi & Steak Dinner Menu

I'm looking for a MENU design with a particular feel. I want to have a base template made that I can then use for future alterations to the menu; ie I can go in and change out different entrees as the menu changes but the template will remain the same. (Ideally it would be in an Apple Pages format.). Also ideally - dinner menu will occupy 2 pages 8.5 x 11. The restaurant's name is Harbor. It is a MODERN steak house that will also feature Sushi, a Raw Bar, Exquisite Cocktails and a sophisticated nightlife crowd. I have attached our LOGO, a secondary logo that we will be featuring throughout the project including on the menu cover (the gold U). Finally - I have attached the content that we would like to see. AGAIN - I REITERATE: High end dining and lounge atmosphere. A couple of restaurants / menus that I love are Morvendel in NYC and Pellucid Steakhouse in Long Island NY. Please do not duplicate - just trying to offer some suggestions.

Requirements
Must have
• A sophisticated and elegant feel without being stuffy or old.

```html
<!DOCTYPE html>
<html lang="en">
<head>
<meta charset="utf-8">
<title>Harbor Sushi &amp; Steak — Dinner Menu</title>
<link href="https://fonts.googleapis.com/css2?family=Figtree:wght@400;700&display=swap" rel="stylesheet">
<style>
  :root {
    --slate: #3a4250;
    --gold: #f2c31c;
    --ink: #ffffff;
    --sketch: #6f7584;
    --ribbon-top: #b9c08c;
    --ribbon-bottom: #b46e57;
    --ribbon-ink: #3a4250;
  }
  html, body { margin: 0; padding: 0; overflow: hidden; }
  body { width: 927px; height: 1200px; background: var(--slate); }
  .menu {
    position: relative; width: 927px; height: 1200px; overflow: hidden;
    background: var(--slate); color: var(--ink);
    font-family: "Figtree", Arial, sans-serif;
  }
  .sketch { position: absolute; background: var(--sketch); opacity: .35; border-radius: 40px; }
  .sketch--corndog { left: 343px; top: 44px; width: 206px; height: 69px; }
  .sketch--fries { left: 694px; top: 258px; width: 182px; height: 206px; }
  .sketch--pizza { left: 305px; top: 950px; width: 173px; height: 170px; }
  .sketch--taco { left: 672px; top: 1043px; width: 195px; height: 137px; border-radius: 100px 100px 30px 30px; }

  .ribbon { position: absolute; left: 772px; top: 0; width: 75px; height: 129px; }
  .ribbon__name {
    position: absolute; left: 0; top: 48px; width: 75px; text-align: center;
    font-weight: 700; font-size: 14px; color: var(--ribbon-ink);
  }

  .section-title {
    position: absolute; margin: 0; font-weight: 700; font-size: 26px;
    line-height: 1; color: var(--gold); letter-spacing: .2px;
  }
  .items { position: absolute; margin: 0; padding: 0; list-style: none; font-size: 16px; line-height: 20.8px; white-space: nowrap; }
  .items li { margin: 0; }
  .items--spaced li { margin-bottom: 8.8px; }
  .items--spaced li.tight { margin-bottom: 0; }
  .gap { margin-top: 20px !important; }
</style>
</head>
<body>
<main class="menu">
  <div class="sketch sketch--corndog" role="img" aria-label="Faint line sketch of a corn dog"></div>
  <div class="sketch sketch--fries" role="img" aria-label="Faint line sketch of fries in a carton"></div>
  <div class="sketch sketch--pizza" role="img" aria-label="Faint line sketch of a pizza slice"></div>
  <div class="sketch sketch--taco" role="img" aria-label="Faint line sketch of a taco"></div>

  <div class="ribbon">
    <svg width="75" height="129" viewBox="0 0 75 129" aria-hidden="true">
      <defs>
        <linearGradient id="ribbonFill" x1="0" y1="0" x2="0" y2="1">
          <stop offset="0" stop-color="var(--ribbon-top)"/>
          <stop offset="1" stop-color="var(--ribbon-bottom)"/>
        </linearGradient>
      </defs>
      <polygon points="0,0 75,0 75,129 37.5,119 0,129" fill="url(#ribbonFill)"/>
    </svg>
    <div class="ribbon__name">Harbor</div>
  </div>

  <h2 class="section-title" style="left:57px;top:103px">APPS</h2>
  <ul class="items" style="left:57px;top:155px">
    <li>BAO Bun; hoisin bbq pancetta cut pork loin,&nbsp; crispy onions, micro mint</li>
    <li>Five Spice Crispy Popcorn Crusted Prawns (2); classic burre blanc</li>
    <li>Jumbo Lump Crab; citrus miso drizzle, spring pea puree, micro greens</li>
    <li>Crispy Wonton Napoleon;&nbsp; cucumber gallete, ahi tuna, jumbo lump crab meat,</li>
    <li>wasabi aioli, shoestring wontons</li>
    <li>PEI Mussels; charred artichoke hearts, blistered heirloom tomatoes, garlic white wine broth</li>
    <li>New Zealand or Domestic Small Eye Lamb Chop (1); crispy porcini risotto cake</li>
  </ul>

  <h2 class="section-title" style="left:56px;top:322px">SALADS</h2>
  <ul class="items items--spaced" style="left:57px;top:364px">
    <li>Classic Wedge; bleu cheese, bacon lardons, heirloom tomatoes</li>
    <li>Mixed Baby Greens; heirloom tomatoes, cucumber, red onion, dijon vinaigrette</li>
    <li class="tight">Tabulleh; buckwheat grain, fresh mint, tomato concasse, cucumber, parsley,</li>
    <li>fresh squeezed lemon, EVOO., salt and pepper</li>
    <li>Tomato Mozzarella Salad / Burratta</li>
    <li class="tight">Spinach Salad; green apple, feta, currants, with per-simmons vinaigrette</li>
    <li>Kale Caesar; homemade cacio e'peppe dressing, pecorino and parmesan cheese, toasted croutons.</li>
  </ul>

  <h2 class="section-title" style="left:56px;top:575px">ENTREES</h2>
  <ul class="items" style="left:57px;top:619px">
    <li>Pan Roasted Miso Glazed Black Cod; green tea noodle stir fry; Napa cabbage, carrot, Japanese eggplant</li>
    <li>Pan Seared Striped Bass; lobster succotash in a tomato saffron broth</li>
    <li>E.V.O.O. Salted / Grilled Swordfish; sun dried tomato, olive and caper tapenade, over basmati rice</li>
    <li>Grilled Half Chicken; sun dried tomato and basil Israeli cous-cous, pan au jus</li>
    <li>Roasted Fresh Caviatelle Ratatoille; vegetable broth</li>
    <li>Lobster Cartoccio; shrimp, mussels, clams, fresh herb tomato broth, tossed with bucatini</li>
    <li>Charred Artichoke Hearts, heirloom tomatoes, caper berries, spring onions, fresh basil,</li>
    <li>white wine reduction over forbidden rice (gf)</li>
    <li class="gap">Mediterranean Grilled Veggie Plate; artichoke hearts, Japanese eggplant, green &amp; white asparagus,</li>
    <li>seared heirloom tomatoes, roasted baby carrots, cauliflower rice, evoo &amp; fig drizzle (gf)</li>
  </ul>

  <h2 class="section-title" style="left:57px;top:890px">USDA PRIME STEAKS (gf)</h2>
  <ul class="items" style="left:57px;top:942px">
    <li>10 Oz Filet 14 or 16 oz</li>
    <li>New York Strip&nbsp; 24 oz</li>
    <li>Boneless Ribeye 36 oz</li>
    <li>Bone in Rib Eye</li>
    <li>Berkshire Pork Chop</li>
  </ul>

  <h2 class="section-title" style="left:555px;top:897px">SAUCES</h2>
  <ul class="items" style="left:555px;top:942px">
    <li>Cabernet Demi Glaz</li>
    <li>Gorganzola Brulle Cream</li>
    <li>Truffled Wild Mushroom Ragu</li>
    <li>Horseradish Cream</li>
    <li>House Steak Sauce</li>
  </ul>

  <h2 class="section-title" style="left:58px;top:1075px">DESSERTS</h2>
  <ul class="items" style="left:58px;top:1120px">
    <li>T.B.D. - separate menu</li>
  </ul>
</main>
</body>
</html>
```